Brochure for a Pilates & Wellness Studio

We are a high end pilates studio. Our target market are high impact professionals who desire the best of the best. Mostly women 35-55+. We offer private training, semi private (up to 4) and group (up to 10) in a class. Our website is www.kelmorastudio-example.com. I'm not great at copy writing and so I don't have great content, unfortunately.

Please call me with any questions - 555-013-7762 MelissaHere's my studio website: www.kelmorastudio-example.com Added Sunday, July 9, 2017

Target Market(s)

high impact working professionals - women. 30-45+

Industry/Entity Type

Health And Wellness

Font styles to use
Sans Serif

Colors
fff3d1
fefdec
f3f1f8

Requirements
Must have
• Service Level Options
• Testimonial (get from Rovix??)
• Why Kelmora Loft
• Benefits of Pilates
• Mind Body Movement Tone - A sense of calm (like a spa brochure would be)
• 50% off Initial Private Intro Session
Nice to have
• Images of us working with clients and the studio

```html
<!DOCTYPE html>
<html lang="en">
<head>
<meta charset="utf-8">
<title>Kelmora Loft – Flyer</title>
<link href="https://fonts.googleapis.com/css2?family=Roboto:wght@300;400;500;700;900&display=swap" rel="stylesheet">
<style>
:root{
  --canvas:#e9e9eb;
  --paper:#ffffff;
  --mist:#ececee;
  --gold-1:#c9b07a;
  --gold-2:#9c8352;
  --slate:#8b8b90;
  --charcoal:#55555a;
  --ink:#2b2b2e;
  --photo-warm-1:#c79a6a;
  --photo-warm-2:#5a4a3e;
  --photo-cool-1:#d6d6d8;
  --photo-cool-2:#6e6e72;
}
*{box-sizing:border-box;margin:0;padding:0}
html,body{width:921px;height:1200px;overflow:hidden}
body{background:var(--canvas);font-family:"Roboto",sans-serif;color:var(--ink);position:relative}
.page{position:absolute;width:430px;height:556px;background:var(--paper);overflow:hidden;box-shadow:0 3px 10px rgba(0,0,0,.18)}
.page--front{left:245px;top:22px}
.page--back{left:245px;top:622px}
.block{position:absolute}
.gold{background:linear-gradient(135deg,var(--gold-1),var(--gold-2))}
.photo{position:absolute}

/* front */
.brand-panel{left:0;top:0;width:250px;height:110px;background:var(--mist)}
.brand{position:absolute;left:28px;top:28px;text-align:right;line-height:1}
.brand__small{display:block;font-weight:300;font-size:20px;letter-spacing:3px;color:var(--gold-2)}
.brand__name{display:block;font-weight:300;font-size:38px;letter-spacing:1px;color:var(--gold-2)}
.stripe{left:0;top:110px;width:430px;height:14px;background:var(--slate)}
.hero-photo{left:0;top:124px;width:430px;height:226px;background:linear-gradient(120deg,var(--photo-warm-2),var(--photo-warm-1) 55%,#e8d6bd)}
.headline-panel{left:0;top:350px;width:430px;height:150px;background:var(--paper)}
.headline{position:absolute;left:150px;top:372px;width:270px;line-height:1.05}
.headline__lead{font-weight:900;font-size:30px;color:var(--ink)}
.headline__rest{font-weight:500;font-size:19px;color:var(--charcoal)}
.headline__gold{font-weight:900;font-size:28px;color:var(--gold-2)}
.front-base{left:0;top:500px;width:430px;height:56px;background:var(--charcoal)}
.url{position:absolute;right:18px;top:519px;color:#fff;font-size:12px;font-weight:500;letter-spacing:.5px}

/* back */
.benefits{left:140px;top:0;width:290px;height:28px}
.benefits__title{position:absolute;left:140px;top:0;width:290px;height:28px;padding:6px 14px;color:#fff;font-weight:700;font-size:14px}
.benefits__list{position:absolute;left:140px;top:28px;width:290px;height:106px;background:var(--slate);padding:7px 14px;list-style:none;color:#fff;font-size:7.2px;line-height:1.55}
.benefits__list li::before{content:"■ ";font-size:6px}
.studio-photo{left:296px;top:134px;width:134px;height:158px;background:linear-gradient(160deg,var(--photo-cool-1),var(--photo-cool-2))}
.testimonial-tab{position:absolute;left:150px;top:142px;background:var(--charcoal);color:#fff;font-weight:700;font-size:13px;padding:4px 12px}
.quote{position:absolute;border:2px solid var(--charcoal);border-radius:8px;padding:14px 9px 9px;font-size:7px;line-height:1.4;color:var(--ink);background:#fff}
.quote::before{content:"\201C";position:absolute;left:6px;top:-10px;font-size:26px;font-weight:900;color:var(--charcoal);background:#fff;line-height:1;padding:0 2px}
.quote::after{content:"\201D";position:absolute;right:6px;bottom:-16px;font-size:26px;font-weight:900;color:var(--charcoal);background:#fff;line-height:1;padding:0 2px}
.quote__name{font-weight:700}
.quote--one{left:12px;top:174px;width:130px;height:86px}
.quote--two{left:152px;top:174px;width:136px;height:86px}
.quote--three{left:302px;top:302px;width:120px;height:88px}
.intro{position:absolute;left:12px;top:272px;width:280px;font-size:7.3px;line-height:1.42;color:var(--charcoal)}
.intro strong{color:var(--gold-2);font-weight:700}
.gold-edge{left:0;top:332px;width:40px;height:16px}
.session-photo{left:0;top:348px;width:300px;height:152px;background:linear-gradient(150deg,var(--photo-cool-1),var(--photo-cool-2))}
.back-rule{left:300px;top:404px;width:130px;height:3px;background:var(--gold-1)}
.back-base{left:0;top:500px;width:430px;height:56px;background:var(--charcoal)}
.contact{position:absolute;left:18px;top:510px;color:#fff;font-size:9px;line-height:1.55;font-style:normal}
.gold-corner{left:380px;top:500px;width:50px;height:56px}
</style>
</head>
<body>

<section class="page page--front">
  <div class="block brand-panel"></div>
  <div class="brand"><span class="brand__small">KELMORA</span><span class="brand__name">LOFT</span></div>
  <div class="block gold" style="left:250px;top:0;width:180px;height:110px"></div>
  <div class="block stripe"></div>
  <div class="photo hero-photo" role="img" aria-label="Instructor leading a reformer pilates class in the studio"></div>
  <div class="block headline-panel"></div>
  <div class="block gold" style="left:370px;top:350px;width:60px;height:34px"></div>
  <div class="block gold" style="left:0;top:420px;width:130px;height:80px"></div>
  <h1 class="headline">
    <span class="headline__lead">High Impact</span><br>
    <span class="headline__rest">professionals who desire the</span><br>
    <span class="headline__gold">best</span> <span class="headline__rest">of the</span> <span class="headline__lead" style="font-size:26px">best</span>
  </h1>
  <div class="block front-base"></div>
  <div class="url">www.kelmorastudio-example.com</div>
</section>

<section class="page page--back">
  <div class="block gold benefits"></div>
  <h2 class="benefits__title">Benefits of Pilates</h2>
  <ul class="benefits__list">
    <li>Private training: one-on-one sessions built around you</li>
    <li>Semi private: up to 4 clients per session</li>
    <li>Group classes: up to 10 clients per class</li>
    <li>Certified instructors with years of training</li>
    <li>Improves posture, balance and core strength</li>
    <li>Calm, spa-like space to reset mind and body</li>
    <li>Flexible scheduling for busy professionals</li>
    <li>50% off your initial private intro session</li>
  </ul>
  <div class="photo studio-photo" role="img" aria-label="Client working on a reformer beside bright studio windows"></div>
  <h2 class="testimonial-tab">Testimonial</h2>
  <blockquote class="quote quote--one">I am completely addicted to this studio. The instructors are kind, skilled and always push me further. <span class="quote__name">Corinne P.</span></blockquote>
  <blockquote class="quote quote--two">I have been attending classes for years and this is the best studio I have found. Truly worth it. <span class="quote__name">Tessa R.</span></blockquote>
  <blockquote class="quote quote--three">I am completely new to pilates, but after three sessions my back pain has eased and I feel stronger. <span class="quote__name">Marlo H.</span></blockquote>
  <p class="intro">At Kelmora Loft, we offer private, semi private and group classes to meet the needs of our clients and our seasoned Pilates goers. Not sure where to start? Book a 60 minute private orientation and we will create a plan that meets your needs and goals. <strong>New clients: 50% off your initial private intro session.</strong> Schedule by appointment.</p>
  <div class="block gold gold-edge"></div>
  <div class="photo session-photo" role="img" aria-label="Instructor guiding a client through a reformer leg exercise"></div>
  <div class="block back-rule"></div>
  <div class="block back-base"></div>
  <div class="block gold gold-corner"></div>
  <address class="contact">
    218 Larkmoor Ave, Fenwick, AZ 85990<br>
    Telephone: 555-014-2281 | Email: hello@kelmorastudio-example.com
  </address>
</section>

</body>
</html>
```